Create company sales sheet to increase referrals so we can get new products

Create a 1 page sales sheet based on the text and logo that we provided.

We are a distribution company. Product manufacturer are a great source of leads for us - as they talk to our potential clients, eg., owners of medical projects, and we are hoping to get referrals.

Keep equal emphasis on each of the trhee words of "Bluefern Carrier Group.

Manufacturers of medical products

It Company

• Equal emphasis on "Bluefern Carrier Group"
• We are expecting a one page one side, but if it looks better, you can make it go to a second page (or double sided)

```html
<!DOCTYPE html>
<html lang="en">
<head>
<meta charset="utf-8">
<title>Bluefern Carrier Group – Sales Sheet</title>
<link rel="stylesheet" href="https://fonts.googleapis.com/css2?family=Oswald:wght@300;400;600&family=Lato:ital,wght@0,400;0,700;1,700&family=Roboto+Condensed:wght@700&display=swap">
<style>
  :root {
    --red: #d71f2b;
    --red-dark: #a3121c;
    --ink: #1d1d1f;
    --charcoal: #2a2a2a;
    --grey-text: #3a3a3a;
    --paper: #ffffff;
  }
  html, body { margin: 0; padding: 0; overflow: hidden; }
  body { width: 900px; height: 1200px; background: var(--paper); }
  .sheet {
    position: relative; width: 900px; height: 1200px; overflow: hidden;
    background: var(--paper); font-family: "Lato", sans-serif; color: var(--grey-text);
  }
  .decor { position: absolute; left: 0; top: 0; }
  .brand { position: absolute; left: 585px; top: 108px; width: 265px; text-align: center; }
  .brand-dot { width: 44px; height: 44px; border-radius: 50%; background: var(--red); margin: 0 auto 10px; }
  .brand-name {
    font-family: "Oswald", sans-serif; font-weight: 400; font-size: 21px;
    letter-spacing: 1px; color: var(--ink); text-transform: uppercase; white-space: nowrap;
  }
  .headline {
    position: absolute; left: 510px; top: 238px; width: 360px; margin: 0; text-align: center;
    font-family: "Oswald", sans-serif; font-weight: inherit; line-height: 1;
  }
  .headline .lead { font-weight: 300; font-size: 38px; color: var(--charcoal); }
  .headline .hot { font-weight: 300; font-size: 60px; color: var(--red); margin-top: 2px; }
  .headline .mid { font-weight: 300; font-size: 36px; color: var(--charcoal); margin-top: 4px; }
  .headline .punch { font-weight: 600; font-size: 50px; color: var(--red); letter-spacing: 2px; margin-top: 2px; }
  .call-band {
    position: absolute; left: 430px; top: 458px; width: 440px; height: 48px;
    display: flex; align-items: center; gap: 20px;
  }
  .call-band .label { font-family: "Roboto Condensed", sans-serif; font-weight: 700; font-size: 30px; color: var(--red); }
  .call-band .number { font-family: "Lato", sans-serif; font-size: 35px; color: #fff; letter-spacing: 1px; }
  .questions {
    position: absolute; right: 40px; top: 548px; text-align: right;
    font-family: "Roboto Condensed", sans-serif; font-weight: 700; font-size: 19px; line-height: 28px;
  }
  .questions .q1 { color: var(--red); }
  .questions .q2 { color: var(--ink); }
  .ribbon {
    position: absolute; right: 0; height: 36px; border-radius: 12px 0 0 12px;
    background: linear-gradient(90deg, var(--red-dark), var(--red) 45%, #e9404a 75%, var(--red));
    color: #fff; font-style: italic; font-weight: 700; font-size: 18px;
    display: flex; align-items: center; justify-content: flex-end; padding-right: 40px; box-sizing: border-box;
    white-space: nowrap;
  }
  .copy {
    position: absolute; right: 40px; margin: 0; text-align: right;
    font-size: 15.5px; line-height: 21px; color: var(--grey-text);
  }
  .web { position: absolute; left: 48px; top: 1150px; color: #fff; font-size: 17px; font-weight: 700; letter-spacing: 2.4px; }
  .address {
    position: absolute; left: 664px; top: 1082px; font-style: normal;
    font-size: 15px; line-height: 19px; color: var(--ink);
  }
  .address svg { position: absolute; left: -34px; top: 4px; }
</style>
</head>
<body>
<main class="sheet">
  <svg class="decor" width="900" height="1200" viewBox="0 0 900 1200">
    <defs>
      <linearGradient id="photoTone" x1="0" y1="0" x2="1" y2="1">
        <stop offset="0" stop-color="#f4f3f8"/>
        <stop offset="0.5" stop-color="#ebe6ef"/>
        <stop offset="1" stop-color="#dde3ea"/>
      </linearGradient>
      <linearGradient id="swooshGrey" x1="0" y1="0" x2="1" y2="0">
        <stop offset="0" stop-color="#cfcfcf"/>
        <stop offset="1" stop-color="#f2f2f2" stop-opacity="0"/>
      </linearGradient>
      <linearGradient id="bandRed" x1="0" y1="0" x2="1" y2="0">
        <stop offset="0" stop-color="#a3121c"/>
        <stop offset="0.6" stop-color="#d71f2b"/>
        <stop offset="1" stop-color="#e8434d"/>
      </linearGradient>
    </defs>

    <path d="M0 700 C 120 900, 350 1080, 640 1140" fill="none" stroke="url(#swooshGrey)" stroke-width="26" opacity="0.7"/>
    <path d="M0 800 C 100 960, 300 1090, 560 1130" fill="none" stroke="#e3e3e3" stroke-width="14"/>
    <path d="M0 900 C 80 1020, 220 1100, 420 1126" fill="none" stroke="#ececec" stroke-width="30"/>

    <path d="M360 0 C 520 90, 520 360, 420 470" fill="none" stroke="#d71f2b" stroke-width="7"/>
    <path d="M400 0 C 560 110, 540 380, 460 460" fill="none" stroke="#1d1d1f" stroke-width="4"/>
    <path d="M435 0 C 570 130, 560 360, 500 450" fill="none" stroke="#d71f2b" stroke-width="2"/>

    <path d="M0 482 C 20 510, 120 540, 230 532 C 360 520, 460 430, 470 300 C 480 160, 410 40, 340 0 L 0 0 Z" fill="#d71f2b"/>
    <path d="M0 500 C 60 540, 180 556, 280 528 C 330 514, 360 500, 380 486" fill="none" stroke="#1d1d1f" stroke-width="6"/>
    <g role="img" aria-label="Photograph: a medical professional in a white coat with a stethoscope touching a glowing interface">
      <path d="M0 460 C 40 500, 130 515, 220 508 C 350 495, 440 410, 446 290 C 452 160, 390 40, 320 0 L 0 0 Z" fill="url(#photoTone)"/>
    </g>

    <path d="M380 506 C 410 470, 430 452, 470 452 L 900 452 L 900 512 L 370 512 Z" fill="#1d1d1f"/>
    <rect x="380" y="446" width="520" height="3" fill="#d71f2b"/>
    <rect x="360" y="515" width="540" height="3" fill="#d71f2b"/>

    <path d="M0 1128 L 560 1128 C 600 1128, 620 1150, 650 1200 L 0 1200 Z" fill="url(#bandRed)"/>
    <path d="M560 1128 C 620 1128, 660 1148, 690 1164 L 900 1164 L 900 1200 L 650 1200 C 630 1160, 600 1136, 560 1128 Z" fill="#1d1d1f"/>
  </svg>

  <header class="brand">
    <div class="brand-dot"></div>
    <div class="brand-name">Bluefern Carrier Group</div>
  </header>

  <h1 class="headline">
    <div class="lead">WE GIVE</div>
    <div class="hot">NEW MEDICAL</div>
    <div class="mid">PRODUCT INNOVATORS</div>
    <div class="punch">A CHANCE</div>
  </h1>

  <div class="call-band">
    <span class="label">CALL US:</span>
    <span class="number">555.014.2280</span>
  </div>

  <div class="questions">
    <div class="q1">Do you have effective products with low sales numbers in need of a distribution partner?</div>
    <div class="q2">Do you have customers with innovative products that need distribution services?</div>
  </div>

  <div class="ribbon" style="top:612px;width:438px;">Bluefern Carrier Group can help!</div>
  <p class="copy" style="top:658px;">Increase your production volume by assisting your customers with product distribution. Bluefern<br>Carrier Group (BCG) specializes in launching new medical products by partnering with<br>medical innovators in bringing new and next generation medical technologies to market.</p>

  <div class="ribbon" style="top:729px;width:658px;">Grow your Manufacturing Enterprise into a Manufacturing Powerhouse.</div>
  <p class="copy" style="top:777px;">Enlighten your customers about BCG and increase manufacturing volumes, as well as earning<br>customer appreciation, loyalty, and referrals.</p>

  <div class="ribbon" style="top:822px;width:218px;">Our Focus.</div>
  <p class="copy" style="top:866px;">We are especially interested in technologies that improve patient care, prevent injury or illness, reduce<br>or mitigate disabilities, save lives, and/or decreases healthcare costs. We look for technologies<br>supported by clinical studies and evidence-based practices.</p>

  <div class="ribbon" style="top:932px;width:499px;">Distribution and Product Launch Support.</div>
  <p class="copy" style="top:976px;">BCG handles all aspects of distribution, product launch, marketing, and sales. We execute creative and<br>effective product launch strategies, using customer motivation psychology combined with targeted and<br>comprehensive client materials, experienced sales force, and extensive global distribution channels.</p>

  <div class="web">www.bluefernscarrier.com</div>

  <address class="address">
    <svg width="26" height="24" viewBox="0 0 26 24" aria-hidden="true">
      <path d="M13 1 L25 12 L21 12 L21 23 L15 23 L15 16 L11 16 L11 23 L5 23 L5 12 L1 12 Z" fill="#a3121c"/>
    </svg>
    Bluefern Carrier Group<br>
    4870 Harbor Point Road,<br>
    Milford, DE 19963
  </address>
</main>
</body>
</html>
```